Sunny Paths and joy Business card

I have a logo, but will like a business card design. Is for a travel agency in Mexico. We focus in family experiences.

I will liek some thing different and unique, from the traditional business card, something to get remmeber for.

Business card information:

Leandro T. Ocampo
leandro@sunnypathsjoy.example

Alameda 482, 3 piso
Col. Tlalpizco
Mexico, D.F. 07320

office: (55) 5000-0142
mobile: (55) 9000-0187

www.sunnypathsjoy.example
@sunnypjoy
blog: sunnypathsandjoy.blogsite.example
facebook: SunnyPathsAndJoy

```html
<!DOCTYPE html>
<html lang="en">
<head>
<meta charset="utf-8">
<title>Sunny Paths and joy — Business card</title>
<link href="https://fonts.googleapis.com/css2?family=Roboto:wght@400;500;700&display=swap" rel="stylesheet">
<style>
  :root {
    --backdrop: #2b2b2d;
    --sky-top: #c9e2f6;
    --sky-mid: #e6f2fb;
    --paper: #ffffff;
    --brand-blue: #2a5aa8;
    --band-top: #3a68b6;
    --band-bottom: #23489a;
    --band-text: #ffffff;
    --logo-tone-a: #8a8178;
    --logo-tone-b: #6c655e;
  }
  * { box-sizing: border-box; margin: 0; padding: 0; }
  html, body { width: 1200px; height: 900px; overflow: hidden; }
  body {
    background: var(--backdrop);
    font-family: "Roboto", Arial, sans-serif;
    position: relative;
  }
  .card {
    position: absolute;
    left: 287px;
    width: 626px;
    height: 382px;
    border-radius: 10px;
    overflow: hidden;
    background: linear-gradient(180deg, var(--sky-top) 0%, var(--sky-mid) 40%, var(--paper) 75%);
    box-shadow: 0 6px 18px rgba(0,0,0,.45);
  }
  .card--front { top: 50px; }
  .card--back { top: 462px; }

  .logo-area {
    position: absolute;
    top: 44px;
    width: 254px;
    height: 184px;
    border-radius: 4px;
    background: linear-gradient(180deg, var(--logo-tone-a), var(--logo-tone-b));
    display: flex;
    align-items: center;
    justify-content: center;
  }
  .card--front .logo-area { left: 333px; }
  .card--back .logo-area { left: 186px; }
  .brand-name {
    color: var(--paper);
    font-weight: 700;
    font-size: 24px;
    text-align: center;
    line-height: 1.15;
  }

  .accent-bar {
    position: absolute; left: 0; top: 85px;
    width: 9px; height: 40px;
    background: var(--brand-blue);
  }
  .person { position: absolute; left: 36px; top: 84px; color: var(--brand-blue); }
  .person-name { font-size: 19px; font-weight: 700; text-transform: uppercase; letter-spacing: .2px; }
  .person-title { font-size: 15px; font-weight: 400; margin-top: 6px; }

  .contact { position: absolute; left: 36px; top: 173px; color: var(--brand-blue); font-size: 13.5px; line-height: 20px; }
  .contact-address { font-weight: 500; }
  .contact-line { display: flex; align-items: center; gap: 9px; font-weight: 400; }
  .contact-line svg { width: 11px; height: 11px; fill: var(--brand-blue); flex: none; }
  .contact-line--email { font-size: 15px; }

  .web-url {
    position: absolute; left: 0; right: 0; top: 268px;
    text-align: center; color: var(--brand-blue); font-size: 19px;
  }

  .social-band {
    position: absolute; left: 0; right: 0; bottom: 0; height: 44px;
    background: linear-gradient(180deg, var(--band-top), var(--band-bottom));
    display: flex; align-items: center; justify-content: center;
    color: var(--band-text); font-size: 13.5px; gap: 10px;
  }
  .social-item { display: flex; align-items: center; gap: 5px; }
  .social-dot { width: 11px; height: 11px; border-radius: 50%; background: var(--band-text); }
  .divider { opacity: .9; }
</style>
</head>
<body>

<section class="card card--front">
  <div class="accent-bar"></div>
  <div class="person">
    <p class="person-name">Leandro T. Ocampo</p>
    <p class="person-title">Director Executive</p>
  </div>

  <div class="contact">
    <p class="contact-address">Alameda 482, 3 piso Col. Tlalpizco</p>
    <p class="contact-address">Mexico, D.F. 07320</p>
    <p class="contact-line"><svg viewBox="0 0 12 12"><path d="M2.5 1 4.5 1 5.3 3.6 4 4.6C4.7 6 6 7.3 7.4 8L8.4 6.7 11 7.5 11 9.5C11 10.3 10.3 11 9.5 11 5 11 1 7 1 2.5 1 1.7 1.7 1 2.5 1Z"/></svg>(55) 5000-0142</p>
    <p class="contact-line"><svg viewBox="0 0 12 12"><path d="M3.5 0.5h5a1 1 0 0 1 1 1v9a1 1 0 0 1-1 1h-5a1 1 0 0 1-1-1v-9a1 1 0 0 1 1-1Zm.5 1.5v7h4V2Z"/></svg>(55) 9000-0187</p>
    <p class="contact-line contact-line--email"><svg viewBox="0 0 12 12"><path d="M1 3h10v6.5H1Zm1 .8 4 3 4-3Z"/></svg>leandro@sunnypathsjoy.example</p>
    <p class="contact-line"><svg viewBox="0 0 12 12"><circle cx="6" cy="6" r="5"/></svg>www.sunnypathsjoy.example</p>
  </div>

  <div class="logo-area" role="img" aria-label="Agency logo artwork area">
    <p class="brand-name">Sunny Paths<br>and joy</p>
  </div>

  <footer class="social-band">
    <span class="social-item"><span class="social-dot"></span>@sunnypjoy</span>
    <span class="divider">|</span>
    <span class="social-item"><span class="social-dot"></span>sunnypathsandjoy.blogsite.example</span>
    <span class="divider">|</span>
    <span class="social-item"><span class="social-dot"></span>SunnyPathsAndJoy</span>
  </footer>
</section>

<section class="card card--back">
  <div class="logo-area" role="img" aria-label="Agency logo artwork area">
    <p class="brand-name">Sunny Paths<br>and joy</p>
  </div>

  <p class="web-url">www.sunnypathsjoy.example</p>

  <footer class="social-band">
    <span class="social-item"><span class="social-dot"></span>@sunnypjoy</span>
    <span class="divider">|</span>
    <span class="social-item"><span class="social-dot"></span>sunnypathsandjoy.blogsite.example</span>
    <span class="divider">|</span>
    <span class="social-item"><span class="social-dot"></span>SunnyPathsAndJoy</span>
  </footer>
</section>

</body>
</html>
```